BRC Business cards

We are a medium sized property company based in London and require a logo, Business card which reflects a professional company and incorporates our catchy name.

Our statement is (Building for the future) we like colours such as royal blue, greens and light browns but will look at anything.

Contact Information for Business Card

Brookcrest Estates Limited
Unit 4, 15-17 Farrowby Lane
London
SE22 7QN

Web: www.brookcrestestates-example.com

Email: brookcrestltd@mailbox-example.com

Telephone: +44-208-555-0142
Fax: +44-208-555-0187

```html
<!DOCTYPE html>
<html lang="en">
<head>
<meta charset="utf-8">
<title>Brookcrest Estates Limited – Business Card</title>
<link rel="stylesheet" href="https://fonts.googleapis.com/css2?family=Ubuntu:wght@400;500;700&display=swap">
<style>
  :root {
    --backdrop: #d8dbde;
    --lime-light: #b8da0c;
    --lime-mid: #aad40e;
    --lime-deep: #98ce18;
    --royal-violet: #5f62a6;
    --ink-violet: #5a5ca4;
    --sand: #ead3ad;
  }
  html, body {
    margin: 0;
    width: 1200px;
    height: 1000px;
    overflow: hidden;
    background: var(--backdrop);
    font-family: "Ubuntu", Arial, sans-serif;
  }
  .business-card {
    position: absolute;
    left: 100px;
    top: 214px;
    width: 1000px;
    height: 572px;
    overflow: hidden;
    box-shadow: 0 10px 30px rgba(0,0,0,0.18);
  }
  .card-facets {
    position: absolute;
    inset: 0;
  }
  .card-details {
    position: absolute;
    left: 80px;
    top: 0;
    color: var(--ink-violet);
  }
  .company-title {
    position: absolute;
    top: 84px;
    left: 0;
    margin: 0;
    font-size: 33px;
    font-weight: 700;
    white-space: nowrap;
  }
  .contact-list {
    position: absolute;
    top: 196px;
    left: 0;
    margin: 0;
    padding: 0;
    list-style: none;
    font-size: 26px;
    font-weight: 500;
    line-height: 37px;
    white-space: nowrap;
  }
  .postal-address {
    position: absolute;
    top: 432px;
    left: 0;
    margin: 0;
    font-size: 26px;
    font-weight: 500;
    font-style: normal;
    white-space: nowrap;
  }
  .brand-name {
    position: absolute;
    right: 34px;
    top: 300px;
    margin: 0;
    color: var(--sand);
    font-size: 34px;
    font-weight: 500;
    line-height: 40px;
    text-align: right;
  }
</style>
</head>
<body>
  <section class="business-card">
    <svg class="card-facets" width="1000" height="572" viewBox="0 0 1000 572" aria-hidden="true">
      <rect width="1000" height="572" fill="var(--lime-light)"/>
      <polygon points="0,300 690,100 700,572 0,572" fill="var(--lime-mid)"/>
      <polygon points="690,100 880,572 240,572" fill="var(--lime-deep)"/>
      <polygon points="740,0 690,100 880,572 1000,572 1000,0" fill="var(--royal-violet)"/>
    </svg>

    <div class="card-details">
      <h1 class="company-title">Brookcrest Estates Limited</h1>
      <ul class="contact-list">
        <li>Telephone: +44-208-555-0142</li>
        <li>Fax: +44-208-555-0187</li>
        <li>Email: brookcrestltd@mailbox-example.com</li>
        <li>Web: www.brookcrestestates-example.com</li>
      </ul>
      <address class="postal-address">Unit 4, 15-17 Farrowby Lane, London SE22 7QN</address>
    </div>

    <p class="brand-name">Brookcrest<br>Estates<br>Limited</p>
  </section>
</body>
</html>
```